Design Business Cards

Please NO GENERIC design submission!

We are a "Mobile Geo Located Advertising and Marketing" company and now we looking for a clean flat modern and simple design for our Business Card.
Our company theme color based Blue and Gray but you can add any accent color to your design.
Our company name is "Plinzo.net".
We have some ideas that could help:
- We like double side card
- We have 3 different logo colors, check attached file
- We need all files as AI file (Editable with Illustrator)

Please feel free to ask us any question you may have.

```html
<!DOCTYPE html>
<html lang="en">
<head>
<meta charset="utf-8">
<title>Plinzo.net Business Card</title>
<link href="https://fonts.googleapis.com/css2?family=Montserrat:wght@700&family=Lato:wght@400;700&display=swap" rel="stylesheet">
<style>
  :root {
    --bg: #3b3c3f;
    --navy: #11293a;
    --blue: #2aa6dc;
    --white: #ffffff;
    --soft: #d7e3ea;
  }
  html, body { margin: 0; padding: 0; overflow: hidden; }
  body {
    width: 1200px; height: 900px;
    background: var(--bg);
    position: relative;
    font-family: "Lato", Arial, sans-serif;
  }
  .card {
    position: absolute;
    width: 560px; height: 320px;
    background: var(--navy);
    border-radius: 22px;
    overflow: hidden;
  }
  .card svg { position: absolute; inset: 0; }
  .card--back { left: 110px; top: 100px; }
  .card--front { left: 530px; top: 470px; }

  .logo {
    position: absolute;
    display: flex; align-items: center; gap: 12px;
  }
  .logo__dot {
    width: 26px; height: 26px; border-radius: 50%;
    background: var(--blue);
  }
  .logo__name {
    font-family: "Montserrat", Arial, sans-serif;
    font-weight: 700;
    color: var(--white);
    letter-spacing: -0.5px;
  }
  .card--back .logo { left: 150px; top: 110px; }
  .card--back .logo__name { font-size: 46px; }
  .website-line {
    position: absolute; left: 215px; top: 212px;
    color: var(--white); font-size: 12px;
  }

  .card--front .logo { right: 40px; top: 42px; }
  .card--front .logo__name { font-size: 38px; }

  .person { position: absolute; left: 40px; top: 120px; padding-left: 16px; }
  .person::before {
    content: ""; position: absolute; left: 0; top: 2px;
    width: 7px; height: 44px; background: var(--white);
  }
  .person__name { color: var(--white); font-weight: 700; font-size: 21px; line-height: 1.1; }
  .person__role {
    color: var(--soft); font-size: 13px; margin-top: 4px;
    padding-bottom: 5px; border-bottom: 1.5px solid var(--white); display: inline-block;
  }

  .contacts { position: absolute; left: 34px; top: 224px; list-style: none; margin: 0; padding: 0; }
  .contacts li {
    display: flex; align-items: center; gap: 10px;
    color: var(--white); font-size: 13px; height: 22px;
  }
  .contacts li.on-blue { color: var(--navy); }
  .contacts svg { position: static; width: 14px; height: 14px; flex: none; }
</style>
</head>
<body>

  <section class="card card--back">
    <svg width="560" height="320" viewBox="0 0 560 320">
      <line x1="60" y1="244" x2="560" y2="160" stroke="#ffffff" stroke-width="1.2"/>
      <polygon points="0,300 300,262 300,320 0,320" fill="#2aa6dc"/>
      <polygon points="320,260 560,230 560,320 320,320" fill="#ffffff"/>
    </svg>
    <div class="logo">
      <span class="logo__dot"></span>
      <span class="logo__name">Plinzo.net</span>
    </div>
    <div class="website-line">www.plinzo.net</div>
  </section>

  <section class="card card--front">
    <svg width="560" height="320" viewBox="0 0 560 320">
      <polygon points="0,176 520,100 520,112 0,204" fill="#2aa6dc"/>
      <polygon points="0,210 560,126 560,133 0,218" fill="#ffffff"/>
      <polygon points="0,222 560,138 560,150 340,200 340,270 0,270" fill="#2aa6dc"/>
    </svg>
    <div class="logo">
      <span class="logo__dot"></span>
      <span class="logo__name">Plinzo.net</span>
    </div>
    <div class="person">
      <div class="person__name">Lena Marwick</div>
      <div class="person__role">Marketing Manager</div>
    </div>
    <ul class="contacts">
      <li class="on-blue">
        <svg viewBox="0 0 24 24"><path d="M6.6 10.8a15.1 15.1 0 0 0 6.6 6.6l2.2-2.2c.3-.3.7-.4 1-.2 1.1.4 2.3.6 3.6.6.6 0 1 .4 1 1V20c0 .6-.4 1-1 1A17 17 0 0 1 3 4c0-.6.4-1 1-1h3.5c.6 0 1 .4 1 1 0 1.3.2 2.5.6 3.6.1.3 0 .7-.2 1z" fill="none" stroke="#11293a" stroke-width="2"/></svg>
        (555) 214 - 3068
      </li>
      <li class="on-blue">
        <svg viewBox="0 0 24 24"><rect x="2" y="5" width="20" height="14" fill="#11293a"/><path d="M2 5l10 8 10-8" fill="none" stroke="#2aa6dc" stroke-width="1.6"/></svg>
        hello@plinzo.net
      </li>
      <li>
        <svg viewBox="0 0 24 24"><path d="M10 14a5 5 0 0 0 7 0l3-3a5 5 0 0 0-7-7l-1 1M14 10a5 5 0 0 0-7 0l-3 3a5 5 0 0 0 7 7l1-1" fill="none" stroke="#ffffff" stroke-width="2.2"/></svg>
        www.plinzo.net
      </li>
      <li>
        <svg viewBox="0 0 24 24"><path d="M12 2a7 7 0 0 0-7 7c0 5 7 13 7 13s7-8 7-13a7 7 0 0 0-7-7zm0 9.5a2.5 2.5 0 1 1 0-5 2.5 2.5 0 0 1 0 5z" fill="#ffffff"/></svg>
        Alpen Route Services GmbH&nbsp; Lindenweg 14 CH-4410
      </li>
    </ul>
  </section>

</body>
</html>
```